Business Card Design Project

I have a two letter domain name qo.com.au (lower case font please). I want a business card, cum logo that is die cut (around the qo segment at least) that fits standard business card size.
qo is all about what 'I am' - a journalist, blogger, analyst, commentator. My mantra is "Writing, analysis & comment.
The reverse of the card only needs my name Lon Fitch, email lon@qo.com.au and mobile +61 400 555 817
Target Market(s)
Mainly people that will use my professional writing services and suppliers that will provide product for review
Industry/Entity Type
Business
Requirements
Must have
- One side is qo.com.au (hint - the .com.au can be vertical or horizontal to fit - the qo should be as large as possible).
The other requires large size font name, email and phone details (so no one needs glasses to read it).
The die cut can be just to highlight the qo segment - need not be around the whole card.
Font used in the past was Belwe (old style - very much like the i used in the information symbol).
Colours - no preference - prefer two colour to process colour but can also be an outline font instead of solid colour.

```html
<!DOCTYPE html>
<html lang="en">
<head>
<meta charset="utf-8">
<title>qo.com.au — Business Card</title>
<link rel="stylesheet" href="https://fonts.googleapis.com/css2?family=Bitter:wght@400;700&display=swap">
<style>
  :root {
    --backdrop: #3b3430;
    --card: #131313;
    --card-edge: #1c1c1c;
    --silver: #a3a3a3;
    --gloss: #4b4b4b;
    --rule: #5a5a5a;
  }
  html, body {
    margin: 0;
    padding: 0;
    width: 1200px;
    height: 716px;
    overflow: hidden;
    background: var(--backdrop);
  }
  .canvas {
    position: relative;
    width: 1200px;
    height: 716px;
    font-family: "Bitter", Georgia, serif;
  }
  .card {
    position: absolute;
    top: 199px;
    width: 520px;
    height: 318px;
    background: var(--card);
    border: 1px solid var(--card-edge);
    border-radius: 3px;
    overflow: hidden;
    box-shadow: 0 14px 30px rgba(0,0,0,0.45);
  }
  .card--front { left: 50px; }
  .card--back  { left: 630px; }

  /* Front: brand name */
  .brand {
    position: absolute;
    left: 40px;
    bottom: 40px;
    display: flex;
    align-items: center;
    gap: 18px;
  }
  .brand__square {
    width: 34px;
    height: 34px;
    background: var(--silver);
  }
  .brand__name {
    margin: 0;
    font-weight: 700;
    font-size: 60px;
    line-height: 1;
    color: var(--silver);
  }

  /* Back: details */
  .tagline {
    position: absolute;
    top: 24px;
    left: 26px;
    display: flex;
    align-items: center;
    gap: 10px;
    font-size: 15px;
    color: var(--silver);
  }
  .tagline__mark { font-weight: 700; }
  .tagline__divider {
    width: 1px;
    height: 18px;
    background: var(--rule);
  }
  .tagline__motto { font-weight: 400; }

  .contact {
    position: absolute;
    left: 26px;
    bottom: 26px;
  }
  .contact__name {
    margin: 0 0 6px;
    font-weight: 700;
    font-size: 34px;
    line-height: 1.1;
    color: var(--silver);
  }
  .contact__line {
    margin: 0;
    font-weight: 400;
    font-size: 31px;
    line-height: 1.25;
    color: var(--gloss);
  }
</style>
</head>
<body>
<main class="canvas">
  <section class="card card--front" aria-label="Card front">
    <div class="brand">
      <span class="brand__square"></span>
      <p class="brand__name">qo.com.au</p>
    </div>
  </section>

  <section class="card card--back" aria-label="Card back">
    <div class="tagline">
      <span class="tagline__mark">qo</span>
      <span class="tagline__divider"></span>
      <span class="tagline__motto">Writing, analysis &amp; comment</span>
    </div>
    <div class="contact">
      <h1 class="contact__name">Lon Fitch</h1>
      <p class="contact__line">lon@qo.com.au</p>
      <p class="contact__line">+61 400 555 817</p>
    </div>
  </section>
</main>
</body>
</html>
```